One page, two sided flyer about our company needed for a conference

We are an IT consulting company and need a two sided flyer produced for our company that we are going to hand out to potential clients at a conference we have coming up.

We would like the design to be in-line with the look and feel of our current website design: www.brinvaroconsulting.example

Our logo has been attached along with some screenshots from our site that we would like included.

Target Market(s)

Business Executives

Industry/Entity Type

It Company

Font styles to use
Sans Serif

Colors
ec1f27

```html
<!DOCTYPE html>
<html lang="en">
<head>
<meta charset="utf-8">
<title>Brinvaro Consulting – Conference Flyer</title>
<link rel="stylesheet" href="https://fonts.googleapis.com/css2?family=Oswald:wght@400;500&family=Roboto:wght@400;500&display=swap">
<style>
  :root {
    --red: #ec1f27;
    --red-deep: #d3242b;
    --black: #0b0b0b;
    --ink: #3a3a3a;
    --grey: #8a8d90;
    --canvas: #ffffff;
    --white: #ffffff;
  }
  * { box-sizing: border-box; margin: 0; padding: 0; }
  html, body { width: 1200px; height: 848px; overflow: hidden; background: var(--canvas); }
  body { position: relative; font-family: "Roboto", Arial, sans-serif; }

  .page {
    position: absolute; top: 38px; width: 534px; height: 754px; overflow: hidden;
    box-shadow: 0 3px 8px rgba(0,0,0,.25);
  }
  .page--front { left: 46px; }
  .page--back { left: 610px; background: var(--white); }
  .page__art { position: absolute; inset: 0; }

  /* Front */
  .brand { position: absolute; left: 34px; top: 44px; color: var(--white); }
  .brand__name { font-family: "Oswald", sans-serif; font-weight: 500; font-size: 42px; line-height: 1; letter-spacing: 1px; }
  .brand__sub { font-size: 15px; letter-spacing: 9.4px; margin-top: 4px; }
  .photo-label { position: absolute; left: 0; top: 170px; width: 534px; height: 320px; }

  .front-headline {
    position: absolute; left: 82px; top: 553px; color: var(--white);
    font-family: "Oswald", sans-serif; font-size: 25px; letter-spacing: .2px;
  }
  .front-tagline { position: absolute; left: 82px; top: 610px; width: 400px; color: var(--white); font-size: 19px; line-height: 1.3; }
  .front-rule { position: absolute; left: 30px; right: 32px; top: 699px; border-top: 1px solid var(--black); }
  .contact { position: absolute; top: 707px; color: var(--white); font-size: 14px; line-height: 1.3; }
  .contact--phone { left: 99px; }
  .contact--email { left: 303px; }

  /* Back */
  .section-title {
    position: absolute; left: 0; right: 0; top: 32px; text-align: center;
    font-family: "Oswald", sans-serif; font-size: 28px; color: #555; letter-spacing: .3px;
  }
  .section-rule { position: absolute; left: 40px; right: 42px; top: 72px; border-top: 1px solid var(--red); }
  .feature { position: absolute; left: 32px; width: 470px; display: flex; gap: 12px; color: var(--ink); font-size: 12.3px; line-height: 1.3; }
  .feature svg { flex: none; width: 38px; height: 38px; }
  .feature__title { text-transform: uppercase; font-size: 12.3px; }
  .feature--1 { top: 86px; }
  .feature--2 { top: 146px; }
  .feature--3 { top: 250px; }

  .service { position: absolute; color: var(--white); font-size: 8.2px; line-height: 1.4; }
  .service__title { font-family: "Oswald", sans-serif; font-size: 16px; color: var(--red); margin-bottom: 6px; line-height: 1.1; }
  .service--managed { left: 105px; width: 340px; top: 416px; text-align: center; }
  .service--implement { left: 20px; width: 168px; top: 566px; text-align: right; }
  .service--implement .service__title { text-align: left; }
  .service--virtual { left: 353px; width: 170px; top: 566px; }
  .service--virtual p + p { margin-top: 7px; }
  .hexes { position: absolute; left: 200px; top: 500px; }
</style>
</head>
<body>

<section class="page page--front">
  <svg class="page__art" viewBox="0 0 534 754" width="534" height="754">
    <rect width="534" height="754" fill="var(--red-deep)"/>
    <rect width="534" height="170" fill="var(--black)"/>
    <polygon points="0,428 267,488 534,428 534,446 267,500 0,446" fill="#9a9ea2"/>
    <polygon points="200,476 267,500 334,476 267,490" fill="#eeeeee"/>
  </svg>
  <div class="brand">
    <div class="brand__name">BRINVARO</div>
    <div class="brand__sub">CONSULTING</div>
  </div>
  <svg class="photo-label" viewBox="0 0 534 320" role="img" aria-label="Photo: four business people in suits walking through a glass walkway">
    <defs>
      <linearGradient id="photoTone" x1="0" y1="0" x2="1" y2="1">
        <stop offset="0" stop-color="#c9d2cf"/>
        <stop offset=".5" stop-color="#8f9a98"/>
        <stop offset="1" stop-color="#5d6466"/>
      </linearGradient>
    </defs>
    <polygon points="0,0 534,0 534,258 267,318 0,258" fill="url(#photoTone)"/>
  </svg>
  <h1 class="front-headline">IT STRATEGY AND IMPLEMENTATION</h1>
  <p class="front-tagline">We take your company to the cutting edge of efficiency.</p>
  <div class="front-rule"></div>
  <div class="contact contact--phone">Phone Number<br>555.010.246</div>
  <div class="contact contact--email">Email<br>info@brinvaroconsulting.example</div>
</section>

<section class="page page--back">
  <svg class="page__art" viewBox="0 0 534 754" width="534" height="754">
    <polygon points="0,328 534,342 534,754 0,754" fill="var(--black)"/>
    <polygon points="170,333 534,342 534,422" fill="var(--red-deep)"/>
    <polygon points="400,680 534,620 534,754 460,754" fill="#2a1213"/>
  </svg>

  <h2 class="section-title">WHAT WE DO</h2>
  <div class="section-rule"></div>

  <div class="feature feature--1">
    <svg viewBox="0 0 38 38"><circle cx="19" cy="19" r="17" fill="none" stroke="var(--red)" stroke-width="2"/><path d="M10 19 L17 26 L30 10" fill="none" stroke="var(--red)" stroke-width="3.5"/></svg>
    <div><div class="feature__title">Experienced Solution Focused Developers</div>All Of Our Developers Have Vast Amounts Of Experience In FlowDesk</div>
  </div>
  <div class="feature feature--2">
    <svg viewBox="0 0 38 38"><circle cx="19" cy="19" r="17" fill="none" stroke="var(--red)" stroke-width="2"/><path d="M10 19 L17 26 L30 10" fill="none" stroke="var(--red)" stroke-width="3.5"/></svg>
    <div><div class="feature__title">Superior Service</div>Our Customers Come First And Our Client Retention Rate Of 98% Proves It. From Word One You Are Our Focus, Whether It Is Providing Alternative Solutions That No One Has Explored, Working With You On A Projects Price, Delivering A Finished Product By A Certain Date Etc.</div>
  </div>
  <div class="feature feature--3">
    <svg viewBox="0 0 38 38"><circle cx="19" cy="19" r="17" fill="none" stroke="var(--red)" stroke-width="2"/><path d="M10 19 L17 26 L30 10" fill="none" stroke="var(--red)" stroke-width="3.5"/></svg>
    <div><div class="feature__title">Competitive Pricing</div>All Solutions Are Presented With Several Delivery Options E.G Full-Time US Developers, A Hybrid Of US + Near Shore, Or All Near Shore.</div>
  </div>

  <div class="service service--managed">
    <div class="service__title">Managed Services</div>
    The key to productivity and efficiency lies in doing only those things which need to be done. But, often companies end-up wasting time struggling with software administration and management; something than can easily be delegated to a third party. This – over a period of time, adds-up to huge operational costs which could have easily been saved.
  </div>

  <svg class="hexes" width="140" height="150" viewBox="0 0 140 150">
    <g fill="var(--red)" stroke="var(--white)" stroke-width="2.5">
      <polygon points="70,2 103,21 103,59 70,78 37,59 37,21"/>
      <polygon points="36,62 69,81 69,119 36,138 3,119 3,81"/>
      <polygon points="104,62 137,81 137,119 104,138 71,119 71,81"/>
    </g>
    <g fill="none" stroke="var(--white)" stroke-width="2">
      <circle cx="66" cy="42" r="11"/>
      <rect x="70" y="26" width="16" height="10" rx="2"/>
      <path d="M26 92 L42 92 L48 100 L38 114 L22 108 Z"/>
      <circle cx="104" cy="93" r="4"/>
      <path d="M94 112 Q104 100 114 112"/>
    </g>
  </svg>

  <div class="service service--implement">
    <div class="service__title">Implementation Services</div>
    Starting from scratch is hard and resource-consuming with any system. That's certainly the case with FlowDesk. You may have heard it can work wonders for your company, but between purchasing the service and setting it up properly is a long stretch of costly trial and error.
  </div>

  <div class="service service--virtual">
    <div class="service__title">Virtual Assistance</div>
    <p>FlowDesk is officially live for your team. The scope and initial deployment is done – your company is excited … Now what?</p>
    <p>Whether you need experts to support your over-burdened Admin team, or a kick-start to enhance your company's instance, we can help you gain back business momentum and ensure your team has all the FlowDesk support you need to achieve your goals.</p>
  </div>
</section>

</body>
</html>
```